Create a Shopify weblayout for Wrenfold Fashion Boutique

I would like a new website layout for my online fashion boutique www.wrenfold-shop.example. My new online boutique is inspired by the 2 English writers of the 19th century. These books come from old English literature. Wrenfold is a fictitious place withing these inspiring love stories. My boutique idea is inspired by old English landscape, unprecedented magic and influenced by bonds between improbable characters. My boutique is for woman initially, but I would like to add male products sometime in the future, hence the logo should be gender neutral.

I have started with a logo which I deciding upon these days. However, the professional website layout that I am looking for would be inspired by a creative visual from the above descriptions.

I do like white/black color scheme, but I would also like the layout to incorporate an additional color plus an additional design element. I was thinking of floral inspirations, like roses or green wine leaves, perhaps. I would like something with a mix of modern, magic, and eclectic. Thank you all in advance for your igniting ideas.
Updates

Project Deadline Extended Reason: Project extended due to holiday season. We are working on submitting feedback regarding our desired layout. Added Thursday, November 24, 2016

Target Market(s)

Online boutique for women and man clothing.

Industry/Entity Type

Fashion

Coding

Coded - Design and coding required

Number of Pages Required

4 page

Font styles to use
Other font styles liked:
• readable, but elegant and artsy

Requirements
Must have
• Elegant, artsy and legible. Embrace the logo (vector files will be uploaded shortly)
• Files must support use with Shopify. More boutique style less commercial. Simple details are nice. I like the efficiency of the commercial sites. Must have a mobile version. EXAMPLE: http://www.mabelsonupperlark.example/ THIS IS A BEAUTIFUL SITE. in place of the yellow line it would be nice to have a vine maybe?
• Although i am stern on this, i don't mean this with any disrespect ever but please, don't call me or email me on my personal email. If we need to connect, we can do so after i pick a design. Thank you.
Nice to have
• It would be nice if the tree of the logo would be incorporate somewhere in the website. We are very much interested in little details. Please inspire us.

```html
<!DOCTYPE html>
<html lang="en">
<head>
<meta charset="utf-8">
<title>Wrenfold Fashion Boutique</title>
<link rel="stylesheet" href="https://fonts.googleapis.com/css2?family=Cinzel:wght@400;700&family=Open+Sans:wght@400;600;700&display=swap">
<style>
:root{
  --frame:#e4e4e4;
  --brick:#f1f1f1;
  --brick-shade:#e8e8e8;
  --white:#ffffff;
  --ink:#1e1e1e;
  --text:#555555;
  --muted:#7a7a7a;
  --line:#cfcfcf;
  --lavender:#9a6ac9;
  --vine:#b99ad9;
  --footer:#f4f4f4;
  --bar:#9b9b9b;
  --wood:#b8844c;
}
*{box-sizing:border-box;margin:0;padding:0}
html,body{width:1200px;height:2403px;overflow:hidden}
body{position:relative;background:var(--frame);font-family:"Open Sans",Arial,sans-serif;color:var(--text)}
.abs{position:absolute}
.panel-brick{left:13px;width:1174px;background:linear-gradient(180deg,var(--brick),var(--brick-shade) 50%,var(--brick))}
.panel-white{left:13px;width:1174px;background:var(--white)}
.header{top:13px;height:844px}
.news{top:857px;height:649px}
.collections{top:1506px;height:657px}
.wordmark{font-family:"Cinzel",Georgia,serif;font-weight:400;color:var(--ink);letter-spacing:1px;line-height:1}
.header-mark{left:101px;top:100px;font-size:50px}
.social{left:1022px;top:132px;display:flex;gap:6px}
.social span{display:block;width:22px;height:22px;border:1.5px solid #666;border-radius:50%}
.vine{left:101px;width:998px;height:30px;background:linear-gradient(180deg,transparent 20%,var(--vine) 45%,#d6c4ea 60%,transparent 85%);opacity:.8;border-radius:15px}
.nav{display:flex;justify-content:center;gap:58px;font-family:"Cinzel",Georgia,serif;font-size:15px;color:var(--muted);letter-spacing:.5px;left:0;width:1200px}
.nav .active{color:var(--ink)}
.main-nav{top:230px}
.hero{left:101px;top:262px;width:998px;height:508px;background:#fff;border-radius:8px;box-shadow:0 4px 10px rgba(0,0,0,.2);padding:5px}
.hero div{width:100%;height:100%;border-radius:6px;background:linear-gradient(135deg,#8a5a2c,var(--wood) 40%,#d6b58a 70%,#a87444)}
.section-title{left:0;width:1200px;display:flex;justify-content:center;align-items:center;gap:12px;font-family:"Cinzel",Georgia,serif;font-weight:700;font-size:19px;color:var(--ink);letter-spacing:.5px}
.section-title .wordmark{font-size:22px;font-weight:400}
.news-card{top:989px;width:316px}
.news-img{height:188px;border-radius:8px;box-shadow:0 6px 10px rgba(0,0,0,.25)}
.news-card h3{margin-top:28px;font-family:"Cinzel",Georgia,serif;font-weight:400;font-size:16px;line-height:21px;color:var(--ink)}
.news-card h3 b{font-weight:700;letter-spacing:1px}
.news-card p{margin-top:15px;font-size:12.5px;line-height:19.5px;color:var(--text)}
.more{margin-top:14px;width:22px;height:22px}
.tab{top:1647px;height:44px;width:291px;display:flex;align-items:center;justify-content:center;font-family:"Cinzel",Georgia,serif;font-weight:700;font-size:15px;letter-spacing:.5px;border-radius:4px 4px 0 0}
.tab-active{left:300px;background:var(--lavender);color:#fff}
.tab-plain{left:609px;background:#fafafa;color:var(--ink);box-shadow:0 -1px 3px rgba(0,0,0,.12)}
.tab-rule{left:101px;top:1691px;width:998px;height:2px;background:#bdbdbd}
.product{top:1729px;width:236px;background:#fff;box-shadow:0 6px 10px rgba(0,0,0,.18)}
.product-img{height:157px}
.product-name{height:45px;display:flex;align-items:center;padding-left:14px;font-size:13px;color:#333;border-bottom:1px solid #e6e6e6}
.product-buy{height:44px;display:flex;align-items:center;justify-content:space-between;padding:0 14px;font-size:12.5px;font-weight:700;color:#333}
.product-buy span{display:flex;align-items:center;gap:6px}
.pager{left:449px;top:2027px;display:flex;border:1px solid #ccc;border-radius:3px;background:#fff}
.pager span{width:28px;height:25px;display:flex;align-items:center;justify-content:center;font-size:13px;color:#555;border-right:1px solid #ddd}
.pager span:last-child{border-right:0}
.pager .current{background:#666;color:#fff;font-weight:700}
.footer-bump{left:384px;top:2118px;width:425px;height:50px;background:var(--footer);border-radius:40px 40px 0 0}
.footer{left:13px;top:2163px;width:1174px;height:195px;background:var(--footer)}
.footer-mark{left:0;width:1200px;top:2210px;text-align:center;font-size:44px}
.footer-rule{left:277px;top:2278px;width:641px;height:1px;background:var(--line)}
.footer-nav{top:2298px;font-size:13.5px}
.copyright{left:13px;top:2358px;width:1174px;height:29px;background:var(--bar);color:#fff;font-size:9px;font-weight:700;display:flex;justify-content:space-between;align-items:center;padding:0 30px}
</style>
</head>
<body>

<section class="abs panel-brick header" role="img" aria-label="Whitewashed brick wall background"></section>
<div class="abs wordmark header-mark">Wrenfold</div>
<div class="abs social" aria-label="Social links"><span></span><span></span><span></span></div>
<div class="abs vine" style="top:178px" role="img" aria-label="Purple flowering vine border"></div>
<nav class="abs nav main-nav">
  <span class="active">Home</span><span>The Team</span><span>Designer Lines</span><span>Events</span><span>News</span><span>Contact Us</span>
</nav>
<div class="abs hero"><div role="img" aria-label="Boutique interior seen from above: wooden floor, clothing rack and display table with denim and accessories"></div></div>
<div class="abs vine" style="top:790px" role="img" aria-label="Purple flowering vine border"></div>

<section class="abs panel-white news"></section>
<h2 class="abs section-title" style="top:914px">What's happening at <span class="wordmark">Wrenfold</span></h2>

<article class="abs news-card" style="left:104px">
  <div class="news-img" role="img" aria-label="Store interior with clothing rails and a pendant lamp" style="background:linear-gradient(180deg,#e9e6e2,#b8b2aa 60%,#3a3633)"></div>
  <h3>News #1<br><b>November 10, 2016</b></h3>
  <p>Lorem ipsum dolor sit amet, consectetuer adipiscing elit, sed diam nonummy nibh euismod tincidunt ut laoreet dolore magna aliquam erat volutpat. Ut wisi enim ad minim veniam, quis nostrud exerci tation ullamcorper suscipit lobortis nisl ut aliquip ex ea commodo consequat.</p>
  <svg class="more" viewBox="0 0 22 22"><circle cx="11" cy="11" r="10" fill="#8a8a8a"/><path d="M6 11h9M11 7l4 4-4 4" stroke="#fff" stroke-width="2" fill="none"/></svg>
</article>
<article class="abs news-card" style="left:442px">
  <div class="news-img" role="img" aria-label="Woman in a dark coat on a rooftop at sunset" style="background:linear-gradient(180deg,#f3efe8,#c9c7c3 55%,#8c8a86)"></div>
  <h3>News #2<br><b>November 8, 2016</b></h3>
  <p>Lorem ipsum dolor sit amet, consectetuer adipiscing elit, sed diam nonummy nibh euismod tincidunt ut laoreet dolore magna aliquam erat volutpat. Ut wisi enim ad minim veniam, quis nostrud exerci tation ullamcorper suscipit lobortis nisl ut aliquip ex ea commodo consequat.</p>
  <svg class="more" viewBox="0 0 22 22"><circle cx="11" cy="11" r="10" fill="#8a8a8a"/><path d="M6 11h9M11 7l4 4-4 4" stroke="#fff" stroke-width="2" fill="none"/></svg>
</article>
<article class="abs news-card" style="left:779px">
  <div class="news-img" role="img" aria-label="Woman in sunglasses sitting among dry grasses under a blue sky" style="background:linear-gradient(180deg,#6d9fd8,#9cbbe0 50%,#6b4a36)"></div>
  <h3>News #3<br><b>November 2, 2016</b></h3>
  <p>Lorem ipsum dolor sit amet, consectetuer adipiscing elit, sed diam nonummy nibh euismod tincidunt ut laoreet dolore magna aliquam erat volutpat. Ut wisi enim ad minim veniam, quis nostrud exerci tation ullamcorper suscipit lobortis nisl ut aliquip ex ea commodo consequat.</p>
  <svg class="more" viewBox="0 0 22 22"><circle cx="11" cy="11" r="10" fill="#8a8a8a"/><path d="M6 11h9M11 7l4 4-4 4" stroke="#fff" stroke-width="2" fill="none"/></svg>
</article>
<div class="abs vine" style="top:1441px" role="img" aria-label="Purple flowering vine border"></div>

<section class="abs panel-brick collections" role="img" aria-label="Whitewashed brick wall background"></section>
<h2 class="abs section-title" style="top:1574px"><span class="wordmark">Wrenfold</span> Latest Collections</h2>
<div class="abs tab tab-active">Women's Clothing</div>
<div class="abs tab tab-plain">Popular Products</div>
<div class="abs tab-rule"></div>

<article class="abs product" style="left:101px">
  <div class="product-img" role="img" aria-label="Model in a dark fur-collared jacket" style="background:linear-gradient(135deg,#2a2c33,#55524f 60%,#2b2622)"></div>
  <div class="product-name">Lorem ipsum dolor sit amet</div>
  <div class="product-buy"><span><svg width="18" height="18" viewBox="0 0 18 18"><circle cx="9" cy="9" r="8" fill="none" stroke="#333" stroke-width="1.3"/><text x="9" y="13" font-size="11" text-anchor="middle" fill="#333" font-family="Arial">$</text></svg>89.00</span><span><svg width="18" height="16" viewBox="0 0 18 16"><path d="M1 2h3l2 8h9l2-6H5" fill="none" stroke="#333" stroke-width="1.5"/><circle cx="7" cy="13.5" r="1.5" fill="#333"/><circle cx="14" cy="13.5" r="1.5" fill="#333"/></svg>Add to cart</span></div>
</article>
<article class="abs product" style="left:354px">
  <div class="product-img" role="img" aria-label="Model in a red jacket and grey hat" style="background:linear-gradient(135deg,#e4e4e4,#c9473a 50%,#d9d9d9)"></div>
  <div class="product-name">Lorem ipsum dolor sit amet</div>
  <div class="product-buy"><span><svg width="18" height="18" viewBox="0 0 18 18"><circle cx="9" cy="9" r="8" fill="none" stroke="#333" stroke-width="1.3"/><text x="9" y="13" font-size="11" text-anchor="middle" fill="#333" font-family="Arial">$</text></svg>59.00</span><span><svg width="18" height="16" viewBox="0 0 18 16"><path d="M1 2h3l2 8h9l2-6H5" fill="none" stroke="#333" stroke-width="1.5"/><circle cx="7" cy="13.5" r="1.5" fill="#333"/><circle cx="14" cy="13.5" r="1.5" fill="#333"/></svg>Add to cart</span></div>
</article>
<article class="abs product" style="left:609px">
  <div class="product-img" role="img" aria-label="Black and white portrait of a model in front of striped blinds" style="background:linear-gradient(180deg,#3a3a3a,#bdbdbd 50%,#5a5a5a)"></div>
  <div class="product-name">Lorem ipsum dolor sit amet</div>
  <div class="product-buy"><span><svg width="18" height="18" viewBox="0 0 18 18"><circle cx="9" cy="9" r="8" fill="none" stroke="#333" stroke-width="1.3"/><text x="9" y="13" font-size="11" text-anchor="middle" fill="#333" font-family="Arial">$</text></svg>34.00</span><span><svg width="18" height="16" viewBox="0 0 18 16"><path d="M1 2h3l2 8h9l2-6H5" fill="none" stroke="#333" stroke-width="1.5"/><circle cx="7" cy="13.5" r="1.5" fill="#333"/><circle cx="14" cy="13.5" r="1.5" fill="#333"/></svg>Add to cart</span></div>
</article>
<article class="abs product" style="left:862px">
  <div class="product-img" role="img" aria-label="Model in a wide-brim hat in a golden field" style="background:linear-gradient(180deg,#4e5a4e,#9b8566 55%,#6b5238)"></div>
  <div class="product-name">Lorem ipsum dolor sit amet</div>
  <div class="product-buy"><span><svg width="18" height="18" viewBox="0 0 18 18"><circle cx="9" cy="9" r="8" fill="none" stroke="#333" stroke-width="1.3"/><text x="9" y="13" font-size="11" text-anchor="middle" fill="#333" font-family="Arial">$</text></svg>49.00</span><span><svg width="18" height="16" viewBox="0 0 18 16"><path d="M1 2h3l2 8h9l2-6H5" fill="none" stroke="#333" stroke-width="1.5"/><circle cx="7" cy="13.5" r="1.5" fill="#333"/><circle cx="14" cy="13.5" r="1.5" fill="#333"/></svg>Add to cart</span></div>
</article>

<nav class="abs pager" aria-label="Pagination">
  <span>&lsaquo;</span><span>1</span><span>2</span><span class="current">3</span><span>4</span><span>5</span><span>6</span><span>7</span><span>8</span><span>9</span><span>&rsaquo;</span>
</nav>

<div class="abs footer-bump"></div>
<footer class="abs footer"></footer>
<div class="abs wordmark footer-mark">Wrenfold</div>
<div class="abs footer-rule"></div>
<nav class="abs nav footer-nav">
  <span class="active">Home</span><span>The Team</span><span>Designer Lines</span><span>Events</span><span>News</span><span>Contact Us</span>
</nav>
<div class="abs copyright"><span>COPYRIGHT © 2016 WRENFOLD. ALL RIGHTS RESERVED.</span><span>TERMS OF USE | PRIVACY STATEMENT</span></div>

</body>
</html>
```